Thistlewood Group Business Card Design

We are looking for a new business card design, we are not happy with our current design. We are a boutique management consulting firm and our clients are typically meridian 400 companies.

I have attached the current front and back that we have as well as a version of our logo that can be used. I am trying to get a higher resolution version of the logo file to upload to the project.

Target Market(s)

Meridian 400 companies are our primary client base. Financial services, life sciences, pharmaceuticals and telecom companies are

Industry/Entity Type

Management Consulting

Contact Information for Business Card

We are trying to communicate a high degree of professionalism, a somewhat minimalist perhaps with some air of whimsy (without overdoing it). Attached is the current design, front and back as well as logos. I like the current back of the card and assume we will keep the phrase the same.

From a color palette perspective, I prefer to stay with a gray scale as they are today.

Font styles to use
Sans Serif

Colors
1b1b1b
474747
ffffff

Requirements
Must have
• Two sided business card design. File format should be something that can be used outside of Photoshop like MS Publisher so that they can be edited with personal information.
• Font should be calibri or something very similar and should be available within MS Office
Should not have
• No other logos or graphics outside of the logo provided.

```html
<!DOCTYPE html>
<html lang="en">
<head>
<meta charset="utf-8">
<title>Thistlewood Group Business Card</title>
<link href="https://fonts.googleapis.com/css2?family=Carlito:wght@400;700&display=swap" rel="stylesheet">
<style>
  :root {
    --ink: #1b1b1b;
    --graphite: #474747;
    --paper: #ffffff;
    --mist: #e9e9e9;
    --stage: #d8d4cf;
  }
  * { margin: 0; padding: 0; box-sizing: border-box; }
  html, body { width: 1200px; height: 1023px; overflow: hidden; }
  body {
    background: var(--stage);
    font-family: "Carlito", "Calibri", sans-serif;
    position: relative;
  }
  .card {
    position: absolute;
    left: 250px;
    width: 700px;
    height: 400px;
    border-radius: 16px;
    overflow: hidden;
    box-shadow: 0 10px 30px rgba(0,0,0,.25);
  }
  .card--front { top: 70px; background: var(--paper); }
  .card--back { top: 550px; background: var(--ink); }

  /* front */
  .brand-area {
    position: absolute; left: 0; top: 0; right: 0; height: 170px;
    background: linear-gradient(180deg, var(--paper), var(--mist));
    display: flex; align-items: center; padding-left: 70px; gap: 22px;
  }
  .brand-dot { width: 44px; height: 44px; border-radius: 50%; background: var(--ink); }
  .brand-name { font-size: 84px; font-weight: 400; color: var(--graphite); letter-spacing: -1px; line-height: 1; }
  .brand-tm { font-size: 12px; color: var(--graphite); align-self: flex-start; margin-top: 42px; margin-left: -14px; }

  .contact-band {
    position: absolute; left: 0; right: 0; top: 170px; bottom: 0;
    background: linear-gradient(90deg, #5a5a5a 0%, var(--graphite) 25%, #2a2a2a 60%, var(--ink) 100%);
    color: var(--paper);
  }
  .divider { position: absolute; left: 44px; right: 44px; top: 92px; height: 1px; background: rgba(255,255,255,.75); }
  .person { position: absolute; left: 44px; top: 56px; font-size: 28px; font-weight: 700; }
  .person .role { font-size: 15px; font-weight: 400; }
  .company { position: absolute; right: 44px; top: 56px; font-size: 28px; font-weight: 700; }
  .details { position: absolute; left: 44px; top: 104px; font-size: 19px; line-height: 1.45; }
  .details li { list-style: none; display: flex; align-items: center; gap: 9px; }
  .details svg { width: 16px; height: 16px; flex: none; }
  .office-line { padding-left: 0; }
  .hq { position: absolute; right: 44px; top: 104px; font-size: 19px; line-height: 1.45; text-align: right; }
  .hq .label { display: flex; justify-content: flex-end; align-items: center; gap: 8px; }
  .hq svg { width: 15px; height: 17px; }

  /* back */
  .back-strip {
    position: absolute; left: 0; right: 0; bottom: 0; height: 54px;
    background: linear-gradient(180deg, var(--paper), #cfcfcf);
    display: flex; align-items: center; justify-content: center;
    color: var(--graphite); font-size: 20px; letter-spacing: 4px;
  }
  .back-mark {
    position: absolute; left: 0; right: 0; top: 0; bottom: 54px;
    display: flex; align-items: center; justify-content: center; gap: 24px;
    background: radial-gradient(circle at 50% 45%, #2b2b2b, var(--ink) 70%);
  }
  .back-mark .brand-dot { background: var(--paper); width: 52px; height: 52px; }
  .back-mark .brand-name { color: var(--paper); font-size: 72px; }
</style>
</head>
<body>

<section class="card card--front" aria-label="Business card front">
  <div class="brand-area">
    <span class="brand-dot"></span>
    <span class="brand-name">Thistlewood</span>
    <span class="brand-tm">TM</span>
  </div>
  <div class="contact-band">
    <p class="person">Mara Ellison, <span class="role">Managing Director</span></p>
    <p class="company">Thistlewood Group, Inc.</p>
    <div class="divider"></div>
    <ul class="details">
      <li class="office-line">Los Angeles Office</li>
      <li>
        <svg viewBox="0 0 16 16" aria-hidden="true"><circle cx="8" cy="8" r="7" fill="none" stroke="#fff" stroke-width="1.3"/><path d="M5.5 4.5c.6-.4 1.1 0 1.4.7l.3.7c.2.4 0 .8-.3 1 .4.9 1 1.5 1.9 1.9.2-.3.6-.5 1-.3l.7.3c.7.3 1.1.8.7 1.4-.6 1-2 .9-3.4-.1-1.2-.8-2.1-1.8-2.6-3-.5-1.3-.4-2.2.3-2.6z" fill="#fff"/></svg>
        206-555-0142
      </li>
      <li>
        <svg viewBox="0 0 16 16" aria-hidden="true"><rect x="1" y="3" width="14" height="10" fill="#fff"/><path d="M1 3l7 6 7-6" fill="none" stroke="#1b1b1b" stroke-width="1.3"/></svg>
        mellison@thistlewoodgroup.com
      </li>
    </ul>
    <div class="hq">
      <p class="label">Headquarters
        <svg viewBox="0 0 15 17" aria-hidden="true"><path d="M7.5 1a5.5 5.5 0 0 1 5.5 5.5c0 4-5.5 9.5-5.5 9.5S2 10.5 2 6.5A5.5 5.5 0 0 1 7.5 1z" fill="none" stroke="#fff" stroke-width="1.3"/><circle cx="7.5" cy="6.5" r="2" fill="#fff"/></svg>
      </p>
      <p>218 Harlow Avenue</p>
      <p>Suite 210, Cedar Point, WA 98000</p>
    </div>
  </div>
</section>

<section class="card card--back" aria-label="Business card back">
  <div class="back-mark">
    <span class="brand-dot"></span>
    <span class="brand-name">Thistlewood</span>
  </div>
  <div class="back-strip">www.thistlewoodgroup.com</div>
</section>

</body>
</html>
```